Christmas Collection Candle Label Design

Looking to update our existing Christmas Candle Collection labels. Labels should reflect the overall feel of our brand- www.kelvabrite.ca
Want to include some color elements. Holiday colors added into design but more muted/ earthy tones not vibrant colors . Metallic elements and line art botanical illustration. Fonts should be more align to brand
Scents
Winter Lantern
Frost Berry
Amber and Fig
Belle Étoile

```html
<!DOCTYPE html>
<html lang="en">
<head>
<meta charset="UTF-8">
<title>Kelvabrite – Belle Étoile Candle Label</title>
<link rel="stylesheet" href="https://fonts.googleapis.com/css2?family=Great+Vibes&family=Libre+Caslon+Display&family=Libre+Caslon+Text&family=Montserrat:wght@400&display=swap">
<style>
  :root {
    --paper: #f3f4f3;
    --ink: #1c1b18;
    --ink-soft: #3b3d42;
    --sketch: #8a7d6e;
    --sketch-light: #d8d1c7;
    --band-dark: #2e2a25;
    --band-light: #6b5f53;
    --band-text: #f1ede6;
  }
  * { margin: 0; padding: 0; box-sizing: border-box; }
  html, body {
    width: 1200px;
    height: 1200px;
    overflow: hidden;
    background: var(--paper);
  }
  .label {
    position: relative;
    width: 1200px;
    height: 1200px;
    background: var(--paper);
    color: var(--ink);
  }
  .botanical {
    position: absolute;
    border-radius: 40%;
    background: radial-gradient(circle, var(--sketch-light) 0%, rgba(216, 209, 199, 0.35) 60%, rgba(243, 244, 243, 0) 100%);
  }
  .botanical--flower { left: 0; top: 0; width: 196px; height: 206px; }
  .botanical--branch { left: 800px; top: 10px; width: 400px; height: 232px; }
  .botanical--cone-left { left: 0; top: 606px; width: 180px; height: 424px; }
  .botanical--cone-right { left: 952px; top: 766px; width: 248px; height: 256px; }

  .brand-name {
    position: absolute;
    top: 98px;
    left: 0;
    width: 100%;
    text-align: center;
    font-family: "Libre Caslon Display", serif;
    font-size: 60px;
    line-height: 1.2;
    letter-spacing: 1px;
    color: var(--ink);
  }
  .tagline {
    position: absolute;
    top: 260px;
    left: 0;
    width: 100%;
    text-align: center;
    font-family: "Montserrat", sans-serif;
    font-size: 37px;
    color: var(--ink-soft);
  }
  .scent-title {
    position: absolute;
    top: 345px;
    left: 0;
    width: 100%;
    text-align: center;
    font-family: "Libre Caslon Display", serif;
    font-weight: 400;
    font-size: 200px;
    line-height: 1;
    color: var(--ink);
  }
  .scent-script {
    position: absolute;
    top: 572px;
    left: 560px;
    font-family: "Great Vibes", cursive;
    font-size: 205px;
    line-height: 1;
    color: var(--ink);
  }
  .scent-notes {
    position: absolute;
    top: 788px;
    left: 0;
    width: 100%;
    text-align: center;
    font-family: "Libre Caslon Text", serif;
    font-size: 40px;
    color: var(--ink);
  }
  .info-bands {
    position: absolute;
    top: 1046px;
    left: 0;
    width: 1200px;
    height: 84px;
    display: flex;
    gap: 12px;
  }
  .info-band {
    flex: 1;
    display: flex;
    align-items: center;
    justify-content: center;
    background: linear-gradient(90deg, var(--band-dark), var(--band-light));
    font-family: "Libre Caslon Text", serif;
    font-size: 29px;
    color: var(--band-text);
  }
</style>
</head>
<body>
  <main class="label">
    <div class="botanical botanical--flower" role="img" aria-label="Line art botanical illustration of an open pine cone flower"></div>
    <div class="botanical botanical--branch" role="img" aria-label="Line art illustration of a pine branch with a pine cone"></div>
    <div class="botanical botanical--cone-left" role="img" aria-label="Line art illustration of a tall pine cone"></div>
    <div class="botanical botanical--cone-right" role="img" aria-label="Line art illustration of a round pine cone"></div>

    <div class="brand-name">KELVABRITE</div>

    <p class="tagline">Made with Plant Based Botanicals</p>

    <h1 class="scent-title">BELLE</h1>
    <div class="scent-script">Étoile</div>

    <p class="scent-notes">Peppercorn - Ginger - Lemon Peel</p>

    <div class="info-bands">
      <div class="info-band">Net Wt 100g</div>
      <div class="info-band">Made in Canada</div>
      <div class="info-band">Natural Soy</div>
    </div>
  </main>
</body>
</html>
```